Existing WP site needs a fresh look (design only)

The current website, www.quorrahub.com.au, is fine, but needs a fresh look so their clients can tell their website has been 'refreshed' regularly.
https://www.quorrahub.com.au/sitemap/
They will use the existing functionality.
They want to keep the blue, green and white of their logo as the main colors, but a fresh look. They prefer a light look to a dark look, but they would be open to good designs that change their mind.
Be creative, think outside the box.
You only need to supply the 'home page ' design to win but the winners will be asked to provide an extra 'standard' page template (like the one currently being used for search results and other pages)
Any photos used must be supplied without charge with the PSDs in a resolution acceptable for the WordPress site.

```html
<!DOCTYPE html>
<html lang="en">
<head>
<meta charset="utf-8">
<title>Quorra Hub – Australia's Top Voices</title>
<link href="https://fonts.googleapis.com/css2?family=Montserrat:wght@300;400;600;700;800&family=Open+Sans:wght@400;600&display=swap" rel="stylesheet">
<style>
:root{
  --green:#7cc242;
  --green-dark:#5fa02c;
  --navy:#163049;
  --navy-deep:#0f2236;
  --ink:#2b3440;
  --muted:#6b7480;
  --light:#f1f2f4;
  --white:#ffffff;
}
*{box-sizing:border-box;margin:0;padding:0}
html,body{width:1200px;height:3944px;overflow:hidden}
body{font-family:"Open Sans",Arial,sans-serif;color:var(--ink);background:var(--white);position:relative}
.abs{position:absolute}
h2.section-title{position:absolute;left:0;width:1200px;text-align:center;font-family:"Montserrat",Arial,sans-serif;font-weight:800;font-size:40px;letter-spacing:1px;color:var(--navy)}
h2.section-title .accent{color:var(--green)}

/* top bar */
.topbar{top:0;left:0;width:1200px;height:32px;background:var(--green);color:var(--white);font-size:13px;font-weight:600;display:flex;justify-content:flex-end;align-items:center;gap:36px;padding-right:40px}
.topbar span{display:flex;align-items:center;gap:6px}
/* nav */
.nav{top:32px;left:0;width:1200px;height:80px;background:var(--navy);display:flex;align-items:center;padding:0 70px}
.brand{font-family:"Montserrat",Arial,sans-serif;font-weight:800;color:var(--white);font-size:26px;display:flex;align-items:center;gap:10px;letter-spacing:1px}
.brand .mark{width:16px;height:16px;background:var(--green)}
.nav ul{list-style:none;display:flex;gap:34px;margin-left:auto;font-family:"Montserrat",Arial,sans-serif;font-size:14px;font-weight:600;color:var(--white);text-transform:uppercase}

/* hero */
.hero{top:112px;left:0;width:1200px;height:748px;background:radial-gradient(circle at 78% 22%,#6a7886 0%,#3a4654 28%,#1d2733 60%,#121a24 100%)}
.hero-title{top:170px;left:112px;color:var(--white);font-family:"Montserrat",Arial,sans-serif}
.hero-title .line1{font-size:46px;font-weight:800;letter-spacing:1px}
.hero-title .line1 .accent{color:var(--green)}
.hero-title .line2{font-size:42px;font-weight:300;letter-spacing:2px;margin-top:2px}
.search-box{top:360px;left:112px;width:470px;height:34px;display:flex}
.search-box .field{flex:1;background:var(--white);font-size:13px;color:#9aa1a9;padding:8px 12px}
.search-box .btn{width:124px;background:var(--green);color:var(--white);font-size:14px;font-weight:600;display:flex;align-items:center;justify-content:center;gap:8px}
.or-badge{top:406px;left:216px;width:32px;height:32px;border-radius:50%;background:var(--green);color:var(--white);font-size:12px;font-weight:700;display:flex;align-items:center;justify-content:center}
.filters{top:488px;left:0;width:1200px;height:260px;background:rgba(15,34,54,.72)}
.select{position:absolute;height:40px;background:var(--white);font-size:13px;color:#6b7480;display:flex;align-items:center;justify-content:space-between;padding:0 14px}
.search-now{top:670px;left:520px;width:160px;height:38px;background:var(--green);color:var(--white);font-size:14px;font-weight:600;display:flex;align-items:center;justify-content:center;gap:8px}

/* spotlight */
.spotlight{top:860px;left:0;width:1200px;height:820px;background:var(--white)}
.artist{position:absolute;top:188px;width:310px}
.artist .photo{height:292px}
.artist .bar{height:108px;background:var(--green);color:var(--white);padding:30px 24px;position:relative}
.artist .name{font-family:"Montserrat",Arial,sans-serif;font-weight:700;font-size:22px}
.artist .loc{font-size:14px;margin-top:4px}
.artist .play{position:absolute;right:22px;top:32px;width:48px;height:48px;border-radius:50%;background:var(--navy)}
.artist p{font-size:14px;line-height:1.6;color:var(--muted);margin-top:30px;padding-right:10px}
.arrow-side{position:absolute;width:40px;height:24px}

/* news */
.news{top:1680px;left:0;width:1200px;height:768px;background:var(--light)}
.news-card{position:absolute;top:192px}
.news-card .photo{height:322px;position:relative}
.news-card .tag{position:absolute;left:0;bottom:0;width:320px;height:92px;background:rgba(124,194,66,.9);color:var(--white);padding:16px 34px}
.news-card .tag .t1{font-family:"Montserrat",Arial,sans-serif;font-weight:700;font-size:22px}
.news-card .tag .t2{font-size:20px}
.news-card .date{font-size:13px;color:var(--muted);margin-top:26px}
.news-card p{font-size:14px;line-height:1.6;color:var(--ink);margin-top:8px}
.read-more{display:inline-flex;width:206px;height:38px;background:var(--green);color:var(--white);font-size:14px;font-weight:600;align-items:center;justify-content:center;gap:8px;margin-top:22px}
.faded{opacity:.35}
.round-arrow{position:absolute;width:40px;height:40px;border-radius:50%;display:flex;align-items:center;justify-content:center}

/* testimonials */
.testimonials{top:2448px;left:0;width:1200px;height:652px;background:var(--white)}
.quote-box{top:124px;left:200px;width:888px;height:468px;background:var(--white);border-top:8px solid var(--green);border-left:8px solid var(--green);box-shadow:0 10px 30px rgba(0,0,0,.08)}
.client-badge{top:130px;left:48px;width:146px;height:146px;border-radius:50%;border:2px solid #d9dde2;display:flex;align-items:center;justify-content:center;font-family:"Montserrat",Arial,sans-serif;font-weight:700;font-size:20px;color:var(--ink)}
.quote-text{top:86px;left:280px;width:520px}
.quote-text .who{font-family:"Montserrat",Arial,sans-serif;font-weight:700;font-size:18px;color:var(--navy)}
.quote-text .role{font-size:13px;color:var(--muted);line-height:1.5;margin-top:4px}
.quote-text p{font-style:italic;font-size:17px;line-height:1.75;color:var(--muted);margin-top:26px}

/* clients */
.clients{top:3100px;left:0;width:1200px;height:340px;background:var(--light)}
.client-row{top:192px;left:192px;display:flex;gap:20px}
.client-tile{width:160px;height:62px;background:var(--white);display:flex;align-items:center;justify-content:center;font-family:"Montserrat",Arial,sans-serif;font-weight:700;font-size:20px;color:var(--navy)}

/* footer */
.footer{top:3440px;left:0;width:1200px;height:504px;background:var(--navy);color:var(--white)}
.footer .brand{position:absolute;top:40px;left:72px;font-size:28px}
.footer .faq{position:absolute;top:220px;left:72px;width:250px;font-size:14px;line-height:1.6;color:var(--green);text-decoration:underline}
.fcol{position:absolute;top:48px}
.fcol h4{font-family:"Montserrat",Arial,sans-serif;font-weight:700;font-size:15px;letter-spacing:1px;margin-bottom:14px;text-transform:uppercase}
.fcol li{list-style:none;font-size:13px;line-height:1.9;color:#cfd7e0}
.contact-line{display:flex;gap:10px;font-size:13px;line-height:1.6;color:#cfd7e0;margin-bottom:12px}
.contact-line .dot{flex:none;width:14px;height:14px;border-radius:50%;background:var(--green);margin-top:3px}
.socials{display:flex;gap:12px;margin-top:20px}
.socials span{width:34px;height:34px;border-radius:50%;background:var(--green)}
.copyright{top:420px;left:0;width:1200px;height:84px;background:var(--navy-deep);font-size:13px;color:#cfd7e0;display:flex;align-items:center;justify-content:center}
.to-top{top:440px;left:1034px;width:46px;height:46px;border-radius:50%;background:var(--green)}
</style>
</head>
<body>

<div class="abs topbar">
  <span><svg width="14" height="14" viewBox="0 0 24 24"><path fill="#fff" d="M6.6 10.8a15 15 0 006.6 6.6l2.2-2.2c.3-.3.7-.4 1-.2 1.1.4 2.3.6 3.6.6.6 0 1 .4 1 1V20c0 .6-.4 1-1 1A17 17 0 013 4c0-.6.4-1 1-1h3.5c.6 0 1 .4 1 1 0 1.3.2 2.5.6 3.6.1.3 0 .7-.2 1z"/></svg>SYDNEY +61 2 9000 1234</span>
  <span><svg width="14" height="14" viewBox="0 0 24 24"><path fill="#fff" d="M6.6 10.8a15 15 0 006.6 6.6l2.2-2.2c.3-.3.7-.4 1-.2 1.1.4 2.3.6 3.6.6.6 0 1 .4 1 1V20c0 .6-.4 1-1 1A17 17 0 013 4c0-.6.4-1 1-1h3.5c.6 0 1 .4 1 1 0 1.3.2 2.5.6 3.6.1.3 0 .7-.2 1z"/></svg>MELBOURNE +61 3 9000 5678</span>
</div>

<header class="abs nav">
  <div class="brand"><span class="mark"></span>QUORRA HUB</div>
  <ul><li>Voices</li><li>Rates</li><li>Payments</li><li>News</li><li>About Us</li><li>Contact</li><li>Shortlist</li></ul>
</header>

<section class="abs hero" role="img" aria-label="Studio microphone in a dark recording booth">
  <div class="abs hero-title">
    <div class="line1">Austral<span class="accent">i</span>a's Top Voices</div>
    <div class="line2">PROFESSIONAL CASTING</div>
  </div>
  <div class="abs search-box">
    <div class="field">Search artist...</div>
    <div class="btn">Search
      <svg width="14" height="14" viewBox="0 0 24 24"><circle cx="10" cy="10" r="7" stroke="#fff" stroke-width="2.5" fill="none"/><path d="M15 15l6 6" stroke="#fff" stroke-width="2.5"/></svg>
    </div>
  </div>
  <div class="abs or-badge">OR</div>
  <div class="abs filters">
    <div class="select" style="top:32px;left:112px;width:308px">Location<span>▾</span></div>
    <div class="select" style="top:32px;left:440px;width:320px">Sex<span>▾</span></div>
    <div class="select" style="top:32px;left:780px;width:308px">Age Range<span>▾</span></div>
    <div class="select" style="top:112px;left:112px;width:308px">Talent Range<span>▾</span></div>
    <div class="select" style="top:112px;left:440px;width:320px">Language<span>▾</span></div>
    <div class="select" style="top:112px;left:780px;width:308px">Accent<span>▾</span></div>
  </div>
  <div class="abs search-now">Search Now
    <svg width="14" height="14" viewBox="0 0 24 24"><circle cx="10" cy="10" r="7" stroke="#fff" stroke-width="2.5" fill="none"/><path d="M15 15l6 6" stroke="#fff" stroke-width="2.5"/></svg>
  </div>
</section>

<section class="abs spotlight">
  <h2 class="section-title" style="top:100px">SPOTL<span class="accent">I</span>GHT</h2>
  <svg class="arrow-side" style="left:38px;top:380px" viewBox="0 0 40 24"><path d="M38 12H4M12 3L3 12l9 9" stroke="#7cc242" stroke-width="2.5" fill="none"/></svg>
  <svg class="arrow-side" style="left:1122px;top:380px" viewBox="0 0 40 24"><path d="M2 12h34M28 3l9 9-9 9" stroke="#163049" stroke-width="2.5" fill="none"/></svg>

  <article class="artist" style="left:112px">
    <div class="photo" role="img" aria-label="Portrait of voice artist Marla Quinby" style="background:linear-gradient(160deg,#7a5b4c,#c9a58e 55%,#e6d3c4)"></div>
    <div class="bar"><div class="name">Marla Quinby</div><div class="loc">Artist - Sydney</div>
      <div class="play"><svg width="48" height="48" viewBox="0 0 48 48"><path d="M19 15l14 9-14 9z" fill="#fff"/></svg></div></div>
    <p>Marla delivers everything from smooth, sultry tones to bright, youthful reads and with a background in advertising</p>
  </article>
  <article class="artist" style="left:442px">
    <div class="photo" role="img" aria-label="Portrait of voice artist Rowan Tillery" style="background:linear-gradient(160deg,#3d2e28,#a27c66 55%,#d8c2b2)"></div>
    <div class="bar"><div class="name">Rowan Tillery</div><div class="loc">Artist - Noosa</div>
      <div class="play"><svg width="48" height="48" viewBox="0 0 48 48"><path d="M19 15l14 9-14 9z" fill="#fff"/></svg></div></div>
    <p>Rowan has a naturally deep timbre to his voice, with the uncanny ability to step out of it and go in numerous directions</p>
  </article>
  <article class="artist" style="left:778px">
    <div class="photo" role="img" aria-label="Portrait of voice artist Zara Fenwick" style="background:linear-gradient(160deg,#2a2a2e,#b9a07a 55%,#ece2cf)"></div>
    <div class="bar"><div class="name">Zara Fenwick</div><div class="loc">Artist - Sydney</div>
      <div class="play"><svg width="48" height="48" viewBox="0 0 48 48"><path d="M19 15l14 9-14 9z" fill="#fff"/></svg></div></div>
    <p>Bright n bubbly, warm &amp; personable, Zara brings all her experience and versatility into the booth.</p>
  </article>
</section>

<section class="abs news">
  <h2 class="section-title" style="top:96px">LATEST NEWS</h2>

  <article class="news-card faded" style="left:-40px;width:320px">
    <div class="photo" role="img" aria-label="Portrait of a featured voice artist" style="background:linear-gradient(160deg,#c9ccd0,#eef0f2)"></div>
    <div class="date">&nbsp;</div>
    <p>Reuben Dalby is the Melbourne voice behind the mic for many years of reads.</p>
    <div class="read-more" style="width:170px;margin-left:40px">Read More</div>
  </article>

  <article class="news-card" style="left:332px;width:536px">
    <div class="photo" role="img" aria-label="Portrait of new voice artist Reuben Haldane" style="background:linear-gradient(160deg,#3e4852,#8f9aa5 50%,#d3d8dd)">
      <div class="tag"><div class="t1">New Voice Alert</div><div class="t2">Reuben Haldane</div></div>
    </div>
    <div class="date">January 8, 2021</div>
    <p>Originally from Bath UK, Reuben has a young fresh British voice with the skill to nail those gnarly regional accents.</p>
    <div style="text-align:center"><div class="read-more">Read More
      <svg width="12" height="12" viewBox="0 0 24 24"><path d="M8 4l8 8-8 8" stroke="#fff" stroke-width="3" fill="none"/></svg></div></div>
  </article>

  <article class="news-card faded" style="left:920px;width:320px">
    <div class="photo" role="img" aria-label="Portrait of a featured voice artist" style="background:linear-gradient(160deg,#9aa0a6,#e4e6e9)">
      <div class="tag" style="width:320px"><div class="t1">New Voice Alert</div><div class="t2">Reuben Dalby</div></div>
    </div>
    <div class="date">January 6, 2021</div>
    <p>We are delighted to introduce another voice to our Melbourne talent roster this week.</p>
    <div class="read-more" style="width:170px;margin-left:110px">Read More</div>
  </article>

  <div class="round-arrow" style="left:110px;top:334px;background:var(--green)"><svg width="14" height="14" viewBox="0 0 24 24"><path d="M16 4l-8 8 8 8" stroke="#fff" stroke-width="3" fill="none"/></svg></div>
  <div class="round-arrow" style="left:1042px;top:334px;background:var(--navy)"><svg width="14" height="14" viewBox="0 0 24 24"><path d="M8 4l8 8-8 8" stroke="#fff" stroke-width="3" fill="none"/></svg></div>
</section>

<section class="abs testimonials">
  <h2 class="section-title" style="top:30px">TESTIMON<span class="accent">I</span>ALS</h2>
  <div class="abs quote-box">
    <div class="abs client-badge">Nine Fathom</div>
    <svg class="abs" style="top:44px;left:760px" width="40" height="32" viewBox="0 0 40 32"><path d="M2 30V18C2 8 7 3 16 1l1 4c-5 2-7 5-7 9h7v16zM23 30V18c0-10 5-15 14-17l1 4c-5 2-7 5-7 9h7v16z" fill="#163049"/></svg>
    <div class="abs quote-text">
      <div class="who">Nine Fathom</div>
      <div class="role">Dane Holloway, Owner<br>Audio Engineer/Sound Designer</div>
      <p>Quorra Hub are a class act all round. Great service, friendly staff and a pool of VO actors that deliver every time I have them in the booth.</p>
    </div>
    <svg class="abs" style="top:390px;left:356px" width="100" height="24" viewBox="0 0 100 24"><path d="M38 12H4M12 3L3 12l9 9" stroke="#7cc242" stroke-width="2.5" fill="none"/><path d="M60 12h34M86 3l9 9-9 9" stroke="#163049" stroke-width="2.5" fill="none"/></svg>
  </div>
</section>

<section class="abs clients">
  <h2 class="section-title" style="top:104px">OUR CL<span class="accent">I</span>ENTS</h2>
  <div class="round-arrow" style="left:128px;top:203px;background:var(--green)"><svg width="14" height="14" viewBox="0 0 24 24"><path d="M16 4l-8 8 8 8" stroke="#fff" stroke-width="3" fill="none"/></svg></div>
  <div class="abs client-row">
    <div class="client-tile">Brindle</div>
    <div class="client-tile">Tallow</div>
    <div class="client-tile" style="font-size:17px">Orchard Lane</div>
    <div class="client-tile">Velline</div>
    <div class="client-tile">Sonara</div>
  </div>
  <div class="round-arrow" style="left:1032px;top:203px;background:var(--navy)"><svg width="14" height="14" viewBox="0 0 24 24"><path d="M8 4l8 8-8 8" stroke="#fff" stroke-width="3" fill="none"/></svg></div>
</section>

<footer class="abs footer">
  <div class="brand"><span class="mark"></span>QUORRA HUB</div>
  <div class="faq">To find out how you can become a quorra artist, please read our FAQs.</div>

  <div class="fcol" style="left:412px">
    <h4>Quick Links</h4>
    <ul><li>Voices</li><li>Rates</li><li>Payments</li><li>News</li><li>About Us</li><li>Contact</li><li>Shortlist</li></ul>
  </div>
  <div class="fcol" style="left:560px;width:300px">
    <h4>Contact Info</h4>
    <div class="contact-line"><span class="dot"></span><span>Quorra Hub Pty Limited</span></div>
    <div class="contact-line"><span class="dot"></span><span>Suite 4, 18 Harbour Lane Kingsford<br>NSW 2032 Australia</span></div>
    <div class="contact-line"><span class="dot"></span><span>Sydney +61 2 9000 1234<br>Melbourne +61 3 9000 5678</span></div>
  </div>
  <div class="fcol" style="left:892px">
    <h4>Others Link</h4>
    <ul><li>Privacy Policy</li><li>Terms and Conditions</li></ul>
    <div class="socials"><span></span><span></span><span></span><span></span></div>
  </div>

  <div class="abs copyright">Copyright © 2021 Quorra Hub Pty Limited. All Rights Reserved.</div>
  <div class="abs to-top"><svg width="46" height="46" viewBox="0 0 46 46"><path d="M16 26l7-7 7 7" stroke="#fff" stroke-width="3" fill="none"/></svg></div>
</footer>

</body>
</html>
```